Sleek modern site for stage hypnotist who does high school, college, university and corporate gigs.

Need a website design for stage hypnotist Mark Dolloway
I'm using a plinkio domain

Mark Dolloway is a stage hypnotist who does high school shows , colleges, corporate and fundraisers
Looking for something sleek and modern looking.
I need about 4 pages at least one main describing what i do
1st page Describes what events i do (high school, college, corporate, weddings, fundraisers, fairs)
2nd page would be an about/bio page
3rd FAQ page about hypnosis.

*what venues do you work with?
*how long is your show?
*How do we promote the show?
*is it safe
*are you insured?
*how much does it cost?
4th page will be a contact page and link to my social media like Snapvue, chirpnet, and possibly Friendlyn.

Included is a few pictures that I'll probably including on the site. I'm waiting on the rest for photoshoot at the this week. Some of these pictures probably will have different stock backgrounds other than grey (something like a las vegas strip or a stage.

Visually I'm looking for a cool color scheme.

Target Market(s)

High school for now but college and corporate down the road.

Industry/Entity Type

Entertainment Industry

Coding

Coded - Design and coding required

Number of Pages Required

4 page

Font styles to use
Serif
Sans Serif

Colors
3277b5
85acd3
9d9d9d
5c5c5c
cbcbcb
aaaaaa
1b1b1b
333333

Requirements
Must have
• MUST BE ABLE TO WORK WITH PLINKIO
• A sleek and professional look as if I've been doing this for years.
• The ability to edit the text of the site so i can improve upon the persuasive parts if need be.
• I also will be getting more promotional photos in the 5 or 6 days after the deadline days so if i pick your project i'd like to be able to integrate some of them into the design. The 3 photos i provided are somewhat place holders to give you an idea of the rest that are to come.
Nice to have
• drop down links
Should not have
• if you zoobit other stage hypnotists their sites are a bit stale and not that modern.

```html
<!DOCTYPE html>
<html lang="en">
<head>
<meta charset="utf-8">
<title>Trancelight Stage – Mark Dolloway, Stage Hypnotist</title>
<link href="https://fonts.googleapis.com/css2?family=Poppins:wght@300;400&family=Questrial&display=swap" rel="stylesheet">
<style>
  :root {
    --ink: #1b1b1b;
    --charcoal: #333333;
    --mid: #5c5c5c;
    --soft: #9d9d9d;
    --pale: #aaaaaa;
    --rule: #cbcbcb;
    --page: #f2f2f2;
    --white: #ffffff;
    --blue: #3277b5;
    --sky: #85acd3;
    --black: #050505;
  }
  * { box-sizing: border-box; margin: 0; padding: 0; }
  html, body { width: 1200px; height: 3136px; overflow: hidden; }
  body {
    position: relative;
    background: var(--page);
    font-family: "Poppins", sans-serif;
    color: var(--mid);
  }
  .abs { position: absolute; }
  .display { font-family: "Questrial", sans-serif; }

  /* Hero */
  .hero { left: 0; top: 0; width: 1200px; height: 590px; overflow: hidden; }
  .hero-photo {
    position: absolute; inset: 0;
    background: radial-gradient(ellipse 520px 360px at 520px 200px, #4a3a32 0%, #241d1a 45%, #0c0c0d 100%);
  }
  .logo {
    left: 63px; top: 16px;
    font-family: "Questrial", sans-serif; font-size: 32px; letter-spacing: 2px;
    color: var(--sky);
  }
  .nav { left: 832px; top: 24px; display: flex; gap: 0; list-style: none; }
  .nav li {
    position: absolute; white-space: nowrap;
    font-family: "Questrial", sans-serif; font-size: 13px; letter-spacing: 1px; color: #d8d8d8;
  }
  .nav .active { color: var(--white); }
  .nav .active::after {
    content: ""; display: block; margin-top: 8px; height: 1px; background: var(--white);
  }
  .hero-kicker {
    left: 0; width: 1200px; top: 240px; text-align: center;
    font-family: "Questrial", sans-serif; font-size: 13px; letter-spacing: 2.5px; color: var(--white);
  }
  .hero-rule { left: 272px; top: 280px; width: 658px; height: 1px; background: rgba(255,255,255,.75); }
  .hero-title {
    left: 0; width: 1200px; top: 290px; text-align: center;
    font-family: "Questrial", sans-serif; font-size: 70px; letter-spacing: 8px; color: var(--white); font-weight: 400;
  }
  .dots { left: 530px; top: 546px; display: flex; gap: 17px; }
  .dots span { width: 13px; height: 13px; border-radius: 50%; background: #8e8e8e; }
  .dots .on { background: var(--white); }

  /* Why choose us */
  .why { left: 63px; top: 652px; width: 1078px; height: 460px; background: var(--white); }
  .why-intro {
    top: 48px; left: 0; width: 100%; text-align: center; font-size: 13px; color: var(--charcoal);
  }
  .why-rule { top: 90px; left: 217px; width: 642px; height: 1px; background: var(--rule); }
  .why-title {
    top: 112px; left: 0; width: 100%; text-align: center;
    font-family: "Questrial", sans-serif; font-size: 29px; color: var(--ink); font-weight: 400;
  }
  .why-copy { left: 46px; width: 986px; font-size: 12.5px; line-height: 22px; color: var(--pale); font-weight: 300; }

  /* Show cards */
  .card { top: 1177px; width: 515px; height: 593px; background: var(--white); }
  .card-photo { position: absolute; left: 0; top: 0; width: 100%; height: 257px; }
  .card-tag {
    position: absolute; top: 296px; width: 100%; text-align: center;
    font-family: "Questrial", sans-serif; font-size: 10.5px; letter-spacing: 3px; color: var(--soft);
  }
  .card-title {
    position: absolute; top: 328px; width: 100%; text-align: center;
    font-family: "Questrial", sans-serif; font-size: 26px; color: var(--ink); font-weight: 400;
  }
  .card-copy {
    position: absolute; left: 54px; top: 386px; width: 400px;
    font-size: 12px; line-height: 22px; color: var(--pale); font-weight: 300;
  }
  .btn {
    position: absolute; display: flex; align-items: center; justify-content: center;
    width: 118px; height: 36px; font-family: "Questrial", sans-serif; font-size: 11px; letter-spacing: 1px;
  }
  .card .btn { left: 209px; top: 501px; border: 1px solid var(--rule); color: var(--charcoal); }

  /* Performer band */
  .band { left: 0; top: 1833px; width: 1200px; height: 295px; background: linear-gradient(90deg, #242424 0%, #2e2e2e 50%, #3a3a3a 100%); overflow: hidden; }
  .band-photo {
    position: absolute; left: 560px; top: 0; width: 640px; height: 295px;
    background: radial-gradient(ellipse 200px 200px at 300px 140px, #6f5d52 0%, #3b3634 55%, rgba(58,58,58,0) 100%);
  }
  .band-kicker {
    left: 119px; top: 78px; font-family: "Questrial", sans-serif; font-size: 12.5px; letter-spacing: 3px; color: #e6e6e6;
  }
  .band-rule { left: 146px; top: 113px; width: 412px; height: 1px; background: #777; }
  .band-name {
    left: 268px; top: 128px; font-family: "Questrial", sans-serif; font-size: 29px; letter-spacing: 2px; color: var(--white); font-weight: 400;
  }
  .band .btn { left: 311px; top: 199px; width: 132px; height: 34px; border: 1px solid #9a9a9a; color: #e6e6e6; }

  /* Hypnosis gallery */
  .gallery-kicker {
    left: 0; width: 1200px; top: 2188px; text-align: center;
    font-family: "Questrial", sans-serif; font-size: 13px; letter-spacing: 3px; color: var(--mid);
  }
  .gallery-title {
    left: 0; width: 1200px; top: 2247px; text-align: center;
    font-family: "Questrial", sans-serif; font-size: 25px; letter-spacing: 3px; color: var(--ink); font-weight: 400;
  }
  .tile { width: 491px; height: 268px; background: var(--white); padding: 17px; }
  .tile div { width: 100%; height: 100%; }

  /* Footer */
  .footer { left: 0; top: 3012px; width: 1200px; height: 124px; background: var(--black); }
  .social { position: absolute; top: 32px; left: 0; width: 100%; display: flex; justify-content: center; gap: 26px; list-style: none; }
  .social li { display: flex; align-items: center; gap: 6px; font-family: "Questrial", sans-serif; font-size: 13px; color: #cfcfcf; }
  .social li::before { content: ""; width: 7px; height: 7px; border-radius: 50%; background: #cfcfcf; }
  .copyright {
    position: absolute; top: 76px; width: 100%; text-align: center;
    font-family: "Questrial", sans-serif; font-size: 12px; letter-spacing: 2px; color: #cfcfcf;
  }
</style>
</head>
<body>

<header class="hero abs">
  <div class="hero-photo" role="img" aria-label="Close-up of open hands holding a monarch butterfly in dim light"></div>
  <div class="logo abs">Trancelight Stage</div>
  <ul class="nav abs">
    <li class="active" style="left:0">HOME</li>
    <li style="left:88px">ABOUT</li>
    <li style="left:173px">FAQ</li>
    <li style="left:248px">CONTACT</li>
  </ul>
  <p class="hero-kicker abs">ADIPISCING LOREM IPSUM FEUGIAT SED PHASELLUS CONSEQUAT</p>
  <div class="hero-rule abs"></div>
  <h1 class="hero-title abs">Lorem Ipsum</h1>
  <div class="dots abs"><span></span><span class="on"></span><span></span><span></span></div>
</header>

<section class="why abs">
  <p class="why-intro abs">Lorem ipsum dolor sit amet consectetur adipiscing elit amet consectetur adipiscing elit.</p>
  <div class="why-rule abs"></div>
  <h2 class="why-title abs">Why Choose Us</h2>
  <p class="why-copy abs" style="top:190px">Lorem ipsum dolor sit amet, consectetur adipiscing elit. Cras at dignissim augue, in iaculis neque. Etiam bibendum felis ac vulputate pellentesque. Cras non blandit quam. Nunc porta, est non posuere sagittis, neque nunc pellentesque diam, a iaculis lacus urna vitae purus. In non dui vel est tempor faucibus. Aliquam erat volutpat. Quisque vel est vitae nibh laoreet auctor. In nec libero dui. Nulla ullamcorper, dolor nec accumsan viverra, libero eros rutrum metus, vel lacinia magna odio non nunc. Praesent semper felis eu rhoncus aliquam. Donec at quam ac libero vestibulum pretium. Nunc faucibus vel arcu in malesuada. Aenean at velit odio. Vestibulum ante ipsum primis in faucibus orci luctus et ultrices posuere cubilia Curae; Maecenas commodo erat eget molestie sollicitudin. Donec imperdiet, ex sed blandit dictum, ipsum metus ultrices arcu, vitae euismod nisl sapien vitae tortor.</p>
  <p class="why-copy abs" style="top:350px">Vivamus nec odio ac ligula congue feugiat at vitae leo. Aenean sem justo, finibus sed dui eu, accumsan facilisis dolor. Fusce quis dui eget odio iaculis aliquam vel sed velit. Nulla pellentesque posuere semper. Nulla eu sagittis lorem, a auctor nulla. Sed ac condimentum orci, ac varius ante. Nunc blandit quam sit amet sollicitudin sodales.</p>
</section>

<article class="card abs" style="left:58px">
  <div class="card-photo" role="img" aria-label="Smiling business audience applauding at a corporate event" style="background:linear-gradient(135deg,#d9d2cb 0%,#c4ab98 45%,#eae6e2 100%)"></div>
  <p class="card-tag">MAECENAS SAPIEN FEUGIAT EX PURUS</p>
  <h3 class="card-title">Corporate Shows</h3>
  <p class="card-copy">Cras aliquet urna ut sapien tincidunt, quis malesuada elit facilisis. Vestibulum sit amet tortor velit. Nam elementum nibh a libero pharetra elementum. Maecenas feugiat ex purus, quis volutpat lacus placerat malesuada.</p>
  <a class="btn">LEARN MORE</a>
</article>

<article class="card abs" style="left:631px">
  <div class="card-photo" role="img" aria-label="Students seated on chairs on a dark stage during a hypnosis show" style="background:linear-gradient(180deg,#2a2a2a 0%,#3d3530 55%,#6b5a4c 80%,#2a2220 100%)"></div>
  <p class="card-tag">MATTIS ELEMENTUM SAPIEN PRETIUM TELLUS</p>
  <h3 class="card-title">High School Shows</h3>
  <p class="card-copy">Cras aliquet urna ut sapien tincidunt, quis malesuada elit facilisis. Vestibulum sit amet tortor velit. Nam elementum nibh a libero pharetra elementum. Maecenas feugiat ex purus, quis volutpat lacus placerat malesuada.</p>
  <a class="btn">LEARN MORE</a>
</article>

<section class="band abs">
  <div class="band-photo" role="img" aria-label="Portrait of the hypnotist in glasses reaching a hand toward the viewer"></div>
  <p class="band-kicker abs">NAM VEL ANTE SIT AMET LIBERO SCELERISQUE FACILISIS</p>
  <div class="band-rule abs"></div>
  <h2 class="band-name abs">Mark Dolloway</h2>
  <a class="btn">GET QUOTE</a>
</section>

<p class="gallery-kicker abs">NAM VEL ANTE SIT AMET LIBERO SCELERISQUE</p>
<h2 class="gallery-title abs">HYPNOSIS - SAFE, RELAXING AND POWERFUL</h2>

<figure class="tile abs" style="left:63px;top:2326px"><div role="img" aria-label="Swinging pocket watch on a chain against black" style="background:radial-gradient(ellipse at 55% 65%,#6e5a3a 0%,#2a2218 40%,#050505 80%)"></div></figure>
<figure class="tile abs" style="left:648px;top:2326px"><div role="img" aria-label="Woman lying relaxed with eyes closed beneath a crystal pendulum" style="background:linear-gradient(120deg,#ededed 0%,#d8cfcb 45%,#c7a99c 65%,#f3f3f3 100%)"></div></figure>
<figure class="tile abs" style="left:63px;top:2677px"><div role="img" aria-label="Extreme close-up of a hazel eye with blue lashes" style="background:radial-gradient(ellipse at 50% 55%,#8a5a30 0%,#b07a66 30%,#d39a8c 60%,#8c5a50 100%)"></div></figure>
<figure class="tile abs" style="left:648px;top:2677px"><div role="img" aria-label="Figure lying back in darkness under a dangling pendulum" style="background:radial-gradient(ellipse at 50% 70%,#5a4a42 0%,#1e1a18 45%,#050505 80%)"></div></figure>

<footer class="footer abs">
  <ul class="social">
    <li>Friendlyn</li>
    <li>chirpnet</li>
    <li>Snapvue</li>
  </ul>
  <p class="copyright">@2018. All Rights Reserved.</p>
</footer>

</body>
</html>
```